Flyer for a mint vending business (KDM). Draft included... need creative mind to complete!

This flyer will be for a mint vending machine business. I am the owner and the flyer will be given to business owners who will be placing the machines in their business for information on the placement. The flyer will be 6" x 9" so the verbiage needs to fit within the size and be readable. I have included a draft of the basic design (both front and back). I would like it to be colorful and eye-catching but professional. I have included the main image of the mint machine (for the front page) in the uploaded files. The KDM logo mentioned on page two is from the business card (also uploaded). The mint image (page one) can be a stock image- would like it to be round, in a silver wrapper and say "Mint" on the front. The information blurbs on the front surrounding the image should have some form of starburst around the text (as shown in the copy with handwritten notes). Creativity input on font, color and background from the designer is appreciated.

```html
<!DOCTYPE html>
<html lang="en">
<head>
<meta charset="utf-8">
<title>Kendale Dual Mints – Placement Flyer</title>
<link rel="stylesheet" href="https://fonts.googleapis.com/css2?family=Anton&family=Oswald:wght@400;500;700&family=Pacifico&family=Montserrat:wght@500;700&display=swap">
<style>
  :root{
    --yellow:#fdc11a;
    --orange:#f7941d;
    --deep-orange:#f26b21;
    --navy:#0e2748;
    --navy-light:#1c3a63;
    --ink:#14213d;
    --white:#ffffff;
    --gold:#f6c21a;
    --red:#c0301d;
  }
  *{margin:0;padding:0;box-sizing:border-box}
  html,body{width:847px;height:1200px;overflow:hidden;background:var(--yellow)}
  .flyer{position:relative;width:847px;height:1200px;overflow:hidden;font-family:"Montserrat",sans-serif}
  .backdrop{position:absolute;inset:0}
  .header{position:absolute;top:48px;left:0;width:100%;display:flex;align-items:center;justify-content:center;gap:22px}
  .badge{width:94px;height:94px;border-radius:50%;background:var(--white);display:flex;align-items:center;justify-content:center;
    font-family:"Anton",sans-serif;font-size:32px;color:var(--deep-orange);letter-spacing:1px}
  .brand-name{font-family:"Anton",sans-serif;color:var(--white);font-size:48px;letter-spacing:1px;white-space:nowrap;font-weight:400}
  .contacts{position:absolute;top:166px;left:0;width:100%;text-align:center;font-family:"Oswald",sans-serif;color:var(--white);font-size:33px;line-height:1.12;font-weight:500}
  .contacts .label{font-weight:400}
  .contacts .line{display:block}
  .contacts .line.second{padding-left:100px}
  .veterans-note{position:absolute;top:254px;left:60px;width:727px;text-align:center;font-size:12.5px;line-height:1.5;color:var(--ink);font-weight:500;text-transform:uppercase}
  .bonus-seal{position:absolute;left:204px;top:400px;width:440px;height:440px}
  .seal-text{position:absolute;left:124px;top:400px;width:600px;height:440px;text-align:center;color:var(--white);white-space:nowrap}
  .seal-and{position:absolute;top:20px;left:0;width:100%;font-family:"Pacifico",cursive;font-size:50px;line-height:1.3}
  .seal-get{position:absolute;top:108px;left:0;width:100%;font-family:"Anton",sans-serif;font-size:84px;line-height:1}
  .seal-yes-row{position:absolute;top:205px;left:0;width:100%;display:flex;justify-content:center;align-items:center;gap:12px}
  .seal-yes{font-family:"Anton",sans-serif;font-size:96px;line-height:1;color:var(--gold)}
  .seal-qualify{font-family:"Anton",sans-serif;font-size:42px;line-height:1.05;text-align:left;letter-spacing:1px}
  .seal-qualify .spaced{letter-spacing:11px}
  .seal-bonus{position:absolute;top:300px;left:0;width:100%;font-family:"Anton",sans-serif;font-size:102px;line-height:1}
  .drawing-box{position:absolute;left:44px;top:866px;width:760px;height:150px;background:var(--gold);border-radius:16px;padding:30px 36px 0;text-align:center;color:var(--ink)}
  .drawing-box p{font-size:16.5px;line-height:1.45;font-weight:500}
  .drawing-box .entry{margin-top:14px;font-weight:700;color:var(--red);font-size:16.5px}
  .closing-note{position:absolute;left:70px;top:1080px;width:707px;text-align:center;color:var(--white);font-size:17.5px;line-height:1.35;font-weight:500}
</style>
</head>
<body>
<main class="flyer">
  <svg class="backdrop" width="847" height="1200" viewBox="0 0 847 1200" aria-hidden="true">
    <defs>
      <linearGradient id="warm" x1="0" y1="0" x2="1" y2="1">
        <stop offset="0" stop-color="#fdb913"/>
        <stop offset="1" stop-color="#f7941d"/>
      </linearGradient>
    </defs>
    <rect width="847" height="1200" fill="url(#warm)"/>
    <path d="M0 0 H420 C300 120 160 140 0 150 Z" fill="#f99a1c" opacity=".7"/>
    <path d="M847 270 C700 330 560 420 420 470 L847 520 Z" fill="#f9a51a"/>
    <path d="M847 300 L847 1200 L0 1200 L0 820 C250 720 520 560 847 300 Z" fill="var(--navy-light)"/>
    <path d="M847 500 L847 1200 L0 1200 L0 940 C300 860 600 760 847 500 Z" fill="var(--navy)"/>
    <path d="M0 560 C120 620 160 720 0 800 Z" fill="#f7b51a" opacity=".6"/>
  </svg>

  <header class="header">
    <div class="badge">KDM</div>
    <h1 class="brand-name">KENDALE DUAL MINTS</h1>
    <div class="badge">KDM</div>
  </header>

  <p class="contacts">
    <span class="line"><span class="label">DIRECT:</span> MARLO: 555-014-2276</span>
    <span class="line second">JESS: 555-014-3391</span>
  </p>

  <p class="veterans-note">We happily support veterans and a donation will be placed on your behalf<br>every month a mint machine is located in your business!</p>

  <svg class="bonus-seal" viewBox="0 0 440 440" aria-hidden="true">
    <circle cx="220" cy="220" r="220" fill="var(--gold)"/>
    <circle cx="220" cy="220" r="200" fill="var(--orange)"/>
    <circle cx="220" cy="220" r="178" fill="var(--navy)"/>
  </svg>
  <div class="seal-text">
    <div class="seal-and">And</div>
    <div class="seal-get">GET PAID?</div>
    <div class="seal-yes-row">
      <span class="seal-yes">YES</span>
      <span class="seal-qualify">QUALIFY<br><span class="spaced">FOR A</span></span>
    </div>
    <div class="seal-bonus">BONUS!</div>
  </div>

  <section class="drawing-box">
    <p>Drawings for cash and prizes! If your location sells specific product<br>goals each month, the business is entered into our half- yearly drawing.</p>
    <p class="entry">EACH MONTH A LOCATION QUALIFIES ADDS AN ADDITIONAL ENTRY!</p>
  </section>

  <p class="closing-note">We find our mint patties sell best in most locations but we are a full service vending operation with the ability to place other types of machines on request. Have questions? have further needs? let us know we'll be happy to assist with any additional vending items</p>
</main>
</body>
</html>
```